BRAVO (Bright Regional Applied Vector Operations) Letter Head Design Project

Company Name: BRAVO (Bright Regional Applied Vector Operations) MFZ.
Office Address: Office No 718, Saffron Crest Block, Palmera Garden Quarter, Dubai, U.A.E
Company line of business:
1) Currently we have a POS solution for retail outlets like duty free shops, supermarkets, department stores etc... The solution is deployed in Harbourline Travel Retail on 350 POS and in Corniche Gate Travel Retail on 100 POS. So our main line of business is the deployment of this solution in retail outlets locally or regionally. We have already deployed the solution in India and Australia.
2) Integration of other third party POS systems with an online credit authorization netwotk in the UAE. This will enable POS applications to connect directly to the acquiring banks without needing an EFT terminal like Paxomat or Tallyrex. The credit card payment is completed at the POS.
3) Other solutions that are targeting retail outlets like mobile POS, queue busting solutions, stock taking solutions using hand held devices, transaction capture systems, etc...
4) Other IT services like support of call center solutions from Bluegrove Systems and development of new solutions as per customer requirements.
We need a letter head design for the company. We don't have any specific requirements in mind and we prefer to leave it up to the designers to come up with creative designs that will not be limited by any guidelines.
Updates
I have just uploaded all the files I received from my company logo designer. Please review and let me know if you need anything else. .
Dear All,
I have received very nice designs and I thank you for all the hard work you have put so far. I would like the letter head to have all the following company details:
Office Address: Office No 718, Saffron Crest Block, MFZ, Dubai UAE
P.O.Box: 58316 Dubai UAE
Tel Number:+971-4-5817730
Fax Number::+971-4-5817731
Website:www.bravomfz.ae
I would also like to represent the company details as a QRCode somewhere on the page, probably next to the company details if possible (as a trial).
In case you have included a butterfly in the middle of the page as part of your design, I prefer that it doesn't include any colors as colors might make reading the text on the page more difficult.
I don't want to have too many butterflies on the page. 2 are more than enough.
Can you also include a design for the continuation pages?
Thank you in advance and I look forward to receiving your creative designs.
Regards
Samir Odeyra

```html
<!DOCTYPE html>
<html lang="en">
<head>
<meta charset="utf-8">
<title>BRAVO Letterhead</title>
<link href="https://fonts.googleapis.com/css2?family=Jura:wght@500;600&display=swap" rel="stylesheet">
<style>
  :root {
    --paper: #ffffff;
    --ink: #231f20;
    --leaf-green: #7cc142;
    --lime: #b4d800;
    --lemon: #e8ea00;
  }
  html, body {
    margin: 0;
    padding: 0;
    overflow: hidden;
    background: var(--paper);
  }
  .letterhead {
    position: relative;
    width: 848px;
    height: 1200px;
    background: var(--paper);
    overflow: hidden;
  }
  .frame-top {
    position: absolute;
    left: 35px;
    top: 90px;
    width: 668px;
    height: 30px;
    background: linear-gradient(90deg, var(--leaf-green), var(--lime) 55%, var(--lemon));
  }
  .frame-left {
    position: absolute;
    left: 35px;
    top: 90px;
    width: 30px;
    height: 585px;
    background: linear-gradient(180deg, var(--leaf-green), var(--leaf-green) 60%, rgba(124, 193, 66, 0.35));
  }
  .frame-bottom-side {
    position: absolute;
    left: 772px;
    top: 835px;
    width: 18px;
    height: 280px;
    background: linear-gradient(180deg, rgba(124, 193, 66, 0.35), var(--leaf-green) 40%);
  }
  .frame-bottom-base {
    position: absolute;
    left: 595px;
    top: 1097px;
    width: 195px;
    height: 18px;
    background: linear-gradient(90deg, rgba(124, 193, 66, 0.35), var(--leaf-green) 40%);
  }
  .brand {
    position: absolute;
    left: 150px;
    top: 158px;
    display: flex;
    align-items: center;
    gap: 18px;
  }
  .brand-dot {
    width: 58px;
    height: 58px;
    border-radius: 50%;
    background: var(--leaf-green);
  }
  .brand-name {
    font-family: "Jura", sans-serif;
    font-weight: 600;
    font-size: 56px;
    line-height: 1;
    letter-spacing: 1px;
    color: var(--ink);
  }
  .office-address {
    position: absolute;
    left: 74px;
    top: 1058px;
    margin: 0;
    font-family: "Jura", sans-serif;
    font-weight: 500;
    font-size: 19.8px;
    line-height: 1.2;
    color: var(--ink);
    white-space: nowrap;
  }
</style>
</head>
<body>
<div class="letterhead">
  <div class="frame-top" role="img" aria-label="Green to yellow corner frame band"></div>
  <div class="frame-left" role="img" aria-label="Green corner frame band"></div>
  <div class="frame-bottom-side" role="img" aria-label="Green lower corner frame band"></div>
  <div class="frame-bottom-base" role="img" aria-label="Green lower corner frame band"></div>

  <div class="brand">
    <span class="brand-dot"></span>
    <span class="brand-name">BRAVO</span>
  </div>

  <p class="office-address">Office No 718, Saffron Crest Block, Palmera Garden Quarter, Dubai, U.A.E</p>
</div>
</body>
</html>
```